Company truck wrap design

We are The Culvert Mending Works - We are looking to have the car wrapped, and need the expertise of a GD.

Below is the logo and photos of the truck.
1. We require an image to be created that offers a before and after of what we do - a story at a glance in essence

2. These images MUST be clean and pop! NO BACKGROUND effects - eg see images attached - we do not want any background imagery simply the pipe.

3. The image attached displays in essence what we require...
Tree roots, broken pipe and then a pipe that has been fixed with our resign (note the green) However,  In place of the green we would like our logo "the swirl" to be placed in the crack of the pipe replacing the single colour green .  We believe this will show exactly what we do in a simple and non verbal way.

4. We would like the images to run along of the upper sides of the canopy - as big as possible but not overpowering in size.

5. The back of the canopy could potentially have the pipe running around the top also. We require the logo contact number and website to be included on all sides

6. The dual cab two doors each side - The doors to display the logo, phone number and the website.

We are open to any suggestions - however - we like clean lines, bold but not overwhelming.

It would  be good to include
(dot points) - the dot could be our logo!
blocked drains
CCTV Inspections
Pipe Relining
Pipe Coating

I have included the brand guide
We are moving on this quickly

The Car is a 2020 HOLT PACER DUAL CAB

We look forward to receiving your work!

Smiles
Marisol

Target Market(s)

Domestic and Commercial buildings

Requirements
Must have
• logo
phone number
website

```html
<!DOCTYPE html>
<html lang="en">
<head>
<meta charset="utf-8">
<title>The Culvert Mending Works – Vehicle Wrap Panels</title>
<link href="https://fonts.googleapis.com/css2?family=Exo+2:ital,wght@0,300;0,400;0,600;1,700;1,800&display=swap" rel="stylesheet">
<style>
  :root {
    --backdrop: #e6e6e6;
    --panel: #1f2021;
    --panel-edge: #151616;
    --cyan: #3fe3dc;
    --mint: #a9efb9;
    --white: #f4f4f4;
    --pipe-dark: #5a5f63;
    --pipe-light: #9aa2a6;
  }
  * { margin: 0; padding: 0; box-sizing: border-box; }
  html, body { width: 1139px; height: 1200px; overflow: hidden; }
  body {
    background: var(--backdrop);
    font-family: "Exo 2", sans-serif;
    color: var(--white);
    position: relative;
  }
  .panel { position: absolute; background: var(--panel); }

  /* ---------- Side canopy ---------- */
  .side-canopy { left: 40px; top: 30px; width: 1059px; height: 320px; border: 3px solid var(--panel-edge); }
  .side-canopy .tier-divider { position: absolute; left: 0; right: 0; top: 155px; height: 4px; background: var(--panel-edge); }
  .chevron { position: absolute; inset: 0; }

  .headline {
    font-style: italic; font-weight: 800; text-transform: uppercase;
    letter-spacing: -1px; line-height: 0.98;
  }
  .headline .lead { color: var(--cyan); display: block; }
  .headline .rest { color: var(--mint); display: block; }
  .side-canopy .headline { position: absolute; left: 28px; top: 16px; font-size: 40px; }

  .services { position: absolute; left: 600px; top: 12px; list-style: none; }
  .services li {
    display: flex; align-items: center; gap: 18px;
    font-style: italic; font-weight: 700; font-size: 29px; line-height: 34px;
  }
  .services .dot { width: 20px; height: 20px; border-radius: 50%; background: var(--cyan); flex: none; }

  .brand { display: flex; align-items: center; }
  .brand .mark { border-radius: 50%; background: var(--cyan); flex: none; }
  .brand .name { font-weight: 300; text-transform: uppercase; line-height: 1.05; color: var(--white); white-space: nowrap; }
  .brand .tagline {
    font-weight: 400; text-transform: uppercase; color: var(--white);
    border-top: 1.5px solid var(--white); white-space: nowrap;
  }

  .side-canopy .brand { position: absolute; left: 30px; top: 190px; gap: 22px; }
  .side-canopy .brand .mark { width: 100px; height: 100px; }
  .side-canopy .brand .name { font-size: 27px; }
  .side-canopy .brand .tagline { font-size: 10px; margin-top: 8px; padding-top: 6px; }

  .contact { position: absolute; white-space: nowrap; }
  .contact .call { color: var(--mint); font-style: italic; font-weight: 800; text-transform: uppercase; line-height: 1; }
  .contact .phone { color: var(--cyan); font-style: italic; font-weight: 800; line-height: 1; letter-spacing: -0.5px; }
  .contact .web { color: var(--white); font-style: italic; font-weight: 700; line-height: 1.1; }
  .side-canopy .contact { left: 600px; top: 170px; }
  .side-canopy .contact .call { font-size: 36px; }
  .side-canopy .contact .phone { font-size: 58px; margin-top: 2px; }
  .side-canopy .contact .web { font-size: 28px; margin-top: 4px; }

  /* ---------- Door ---------- */
  .door { left: 270px; top: 385px; width: 600px; height: 200px; border-radius: 6px; }
  .door .brand { position: absolute; left: 30px; top: 40px; gap: 20px; }
  .door .brand .mark { width: 110px; height: 110px; }
  .door .brand .name { font-size: 28px; }
  .door .brand .tagline { font-size: 11px; margin-top: 8px; padding-top: 7px; }
  .door .contact { left: 360px; top: 58px; }
  .door .contact .call { font-size: 20px; }
  .door .contact .phone { font-size: 32px; margin-top: 4px; }
  .door .contact .web { font-size: 15px; margin-top: 6px; }

  /* ---------- Rear canopy ---------- */
  .rear-canopy {
    left: 170px; top: 615px; width: 800px; height: 560px;
    clip-path: polygon(12% 0, 88% 0, 100% 16%, 100% 100%, 0 100%, 0 16%);
  }
  .rear-canopy .door-face {
    position: absolute; left: 80px; right: 80px; top: 28px; bottom: 28px;
    border: 3px solid var(--panel-edge);
  }
  .rear-canopy .brand { position: absolute; left: 165px; top: 52px; gap: 36px; }
  .rear-canopy .brand .mark { width: 160px; height: 160px; }
  .rear-canopy .brand .name { font-size: 36px; }
  .rear-canopy .brand .tagline { font-size: 13px; margin-top: 10px; padding-top: 9px; }
  .rear-canopy .rule { position: absolute; left: 115px; right: 115px; top: 285px; height: 2px; background: var(--cyan); }
  .rear-canopy .headline { position: absolute; left: 115px; top: 315px; font-size: 32px; }
  .rear-canopy .contact { left: 440px; top: 315px; }
  .rear-canopy .contact .call { font-size: 30px; }
  .rear-canopy .contact .phone { font-size: 42px; margin-top: 2px; }
  .rear-canopy .contact .web { font-size: 20px; margin-top: 2px; }

  .pipe-story {
    position: absolute; left: 115px; right: 115px; top: 445px; height: 62px;
    border-radius: 31px;
    background: linear-gradient(90deg, var(--pipe-dark) 0%, var(--pipe-light) 48%, var(--cyan) 52%, var(--mint) 100%);
  }
</style>
</head>
<body>

  <!-- Side canopy panel -->
  <section class="panel side-canopy">
    <div class="tier-divider"></div>
    <svg class="chevron" viewBox="0 0 1053 314" preserveAspectRatio="none" aria-hidden="true">
      <polyline points="551,0 402,157 519,314" fill="none" stroke="var(--cyan)" stroke-width="5"/>
      <line x1="505" y1="55" x2="462" y2="100" stroke="var(--mint)" stroke-width="5"/>
      <line x1="462" y1="215" x2="495" y2="255" stroke="var(--cyan)" stroke-width="5"/>
    </svg>

    <h2 class="headline"><span class="lead">We are the</span><span class="rest">Culvert Mending</span><span class="rest">Works</span></h2>

    <ul class="services">
      <li><span class="dot"></span>Blocked Drains</li>
      <li><span class="dot"></span>CCTV Inspections</li>
      <li><span class="dot"></span>Pipe Relining</li>
      <li><span class="dot"></span>Pipe Coating</li>
    </ul>

    <div class="brand">
      <span class="mark"></span>
      <div>
        <p class="name">The Culvert<br>Mending<br>Works</p>
        <p class="tagline">No dig pipe repairs</p>
      </div>
    </div>

    <div class="contact">
      <p class="call">Call us</p>
      <p class="phone">0123 456 789</p>
      <p class="web">www.yourwebsite.com</p>
    </div>
  </section>

  <!-- Cab door panel -->
  <section class="panel door">
    <div class="brand">
      <span class="mark"></span>
      <div>
        <p class="name">The Culvert<br>Mending<br>Works</p>
        <p class="tagline">No dig pipe repairs</p>
      </div>
    </div>
    <div class="contact">
      <p class="call">Call us</p>
      <p class="phone">0123 456 789</p>
      <p class="web">www.yourwebsite.com</p>
    </div>
  </section>

  <!-- Rear canopy panel -->
  <section class="panel rear-canopy">
    <div class="door-face"></div>
    <div class="brand">
      <span class="mark"></span>
      <div>
        <p class="name">The Culvert<br>Mending<br>Works</p>
        <p class="tagline">No dig pipe repairs</p>
      </div>
    </div>
    <div class="rule"></div>
    <h2 class="headline"><span class="lead">We are the</span><span class="rest">Culvert Mending</span><span class="rest">Works</span></h2>
    <div class="contact">
      <p class="call">Call us</p>
      <p class="phone">0123 456 789</p>
      <p class="web">www.yourwebsite.com</p>
    </div>
    <div class="pipe-story" role="img" aria-label="Before and after illustration: a pipe cracked by tree roots, then the same pipe sealed with relining resin"></div>
  </section>

</body>
</html>
```